Hamper box design

We are a chocolate business and need a sophisticated, premium hamper box design. Our hamper box is black and we tie a ribbon on the outside (please see attached photo).

Requirements:
- Incorporate our logo or picture of bean on the top surface of the hamper box
- Need a design for the inside of the top lid (see attachment "Inside Design" for an example)

The dimensions of the actual hamper boxes (need the correct files for these sizes):
1. 240mm wide x 210mm long x 60mm deep.
2. 340mm wide x 260mm long x 90mm deep.
3. 420mm wide x 330mm long x 110mm deep.

Suggestions (not essential):
- Where Chocolate Meets Craftmanship (our slogan)
- The smoothest French chocolate experience
- A thin gold border styling on the top and/or inside surface (to give sophisticated feel) See "Bertrand Olsavik border" file
- Follow us:
(instagram symbol) @corvellinotruffles
(facebook symbol) plumora.net/corvellinotruffles
(world symbol) www.corvellinotruffles.com.au

Our website is: www.corvellinotruffles.com.au
Potential inspiration from our snapvue.net/corvellinotruffles

```html
<!DOCTYPE html>
<html lang="en">
<head>
<meta charset="utf-8">
<title>Corvellino Truffles – Hamper Lid</title>
<link rel="stylesheet" href="https://fonts.googleapis.com/css2?family=Cormorant+Garamond:ital,wght@1,500&family=Source+Sans+3:wght@400&family=Ubuntu:wght@400&display=swap">
<style>
  :root {
    --ink: #0b0b0b;
    --charcoal: #1c1c1c;
    --gold: #f2b877;
    --gold-line: #b98a52;
    --band-dark: #7b5a2c;
    --band-mid: #b08b55;
    --band-light: #ffc27c;
    --band-text: #1a1208;
  }
  html, body {
    margin: 0;
    padding: 0;
    width: 1200px;
    height: 1050px;
    overflow: hidden;
    background: var(--ink);
  }
  .lid {
    position: relative;
    width: 1200px;
    height: 1050px;
    overflow: hidden;
    background: var(--ink);
  }
  .lid__photo {
    position: absolute;
    inset: 0 0 78px 0;
    background:
      radial-gradient(ellipse 46% 52% at 50% 52%, #262626 0%, #161616 55%, transparent 100%),
      radial-gradient(ellipse 90% 80% at 50% 45%, var(--charcoal) 0%, #0d0d0d 70%, #050505 100%);
  }
  .lid__brand {
    position: absolute;
    top: 178px;
    left: 0;
    width: 100%;
    margin: 0;
    text-align: center;
    font-family: "Cormorant Garamond", serif;
    font-style: italic;
    font-weight: 500;
    font-size: 34px;
    color: var(--gold);
    letter-spacing: 0.5px;
  }
  .lid__rule { position: absolute; }
  .lid__rule--left { left: 126px; top: 190px; }
  .lid__rule--right { left: 1010px; top: 560px; }
  .lid__slogan {
    position: absolute;
    top: 486px;
    left: 0;
    width: 100%;
    margin: 0;
    text-align: center;
    font-family: "Cormorant Garamond", serif;
    font-style: italic;
    font-weight: 500;
    font-size: 56px;
    line-height: 1;
    color: var(--gold);
  }
  .lid__tagline {
    position: absolute;
    top: 570px;
    left: 0;
    width: 100%;
    margin: 0;
    text-align: center;
    font-family: "Source Sans 3", sans-serif;
    font-size: 20px;
    color: var(--gold);
  }
  .lid__flourish {
    position: absolute;
    left: 547px;
    top: 830px;
    width: 106px;
    height: 22px;
    border-radius: 11px;
    background: linear-gradient(90deg, rgba(242,184,119,0.15), rgba(242,184,119,0.55), rgba(242,184,119,0.15));
  }
  .lid__contacts {
    position: absolute;
    left: 0;
    bottom: 0;
    width: 100%;
    height: 78px;
    display: flex;
    align-items: center;
    justify-content: center;
    gap: 24px;
    background: linear-gradient(90deg, var(--band-mid) 0%, var(--band-dark) 18%, #a98451 38%, var(--band-light) 62%, #c49659 82%, var(--band-dark) 100%);
    font-family: "Ubuntu", sans-serif;
    font-size: 15px;
    color: var(--band-text);
  }
  .lid__divider { font-weight: 400; }
</style>
</head>
<body>
<main class="lid">
  <div class="lid__photo" role="img" aria-label="Dark background photo of broken squares of dark chocolate on a textured black surface"></div>

  <p class="lid__brand">Corvellino Truffles</p>

  <svg class="lid__rule lid__rule--left" width="54" height="250" viewBox="0 0 54 250" aria-hidden="true">
    <line x1="16" y1="0" x2="16" y2="245" stroke="var(--gold-line)" stroke-width="2"/>
    <line x1="5" y1="218" x2="52" y2="218" stroke="var(--gold-line)" stroke-width="2"/>
  </svg>

  <h1 class="lid__slogan">Where Chocolate Meets Craftmanship</h1>
  <p class="lid__tagline">The smoothest French chocolate experience</p>

  <svg class="lid__rule lid__rule--right" width="70" height="286" viewBox="0 0 70 286" aria-hidden="true">
    <line x1="47" y1="0" x2="47" y2="284" stroke="var(--gold-line)" stroke-width="2"/>
    <line x1="2" y1="273" x2="67" y2="273" stroke="var(--gold-line)" stroke-width="2"/>
  </svg>

  <div class="lid__flourish" role="img" aria-label="Small gold scroll ornament"></div>

  <footer class="lid__contacts">
    <span>www.corvellinotruffles.com.au</span>
    <span class="lid__divider">|</span>
    <span>info@corvellinotruffles.com.au</span>
    <span class="lid__divider">|</span>
    <span>@corvellinotruffles</span>
    <span class="lid__divider">|</span>
    <span>plumora.net/corvellinotruffles</span>
  </footer>
</main>
</body>
</html>
```